Dalton Wire Supply, Inc. Business Card Design

We are an Electrical Distributor looking for a Modern, Professional Business Card design.

Target Market(s)

Residential Commercial Industrial

Industry/Entity Type

Electrical

Contact Information for Business Card

Dalton Wire Supply, Inc.
418 Birchwood Lane
Millbrook, VA 24512
540-555-2741
540-555-8196 Fax
daltonwire@pinemail.example

```html
<!DOCTYPE html>
<html lang="en">
<head>
<meta charset="utf-8">
<title>Dalton Wire Supply, Inc. — Business Card</title>
<link href="https://fonts.googleapis.com/css2?family=Open+Sans:wght@400;600&display=swap" rel="stylesheet">
<style>
  :root {
    --backdrop: #e9e7e4;
    --card: #29333c;
    --card-edge: #232c34;
    --accent: #f07a2c;
    --text: #ffffff;
    --text-soft: #e6e9ec;
  }
  * { margin: 0; padding: 0; box-sizing: border-box; }
  html, body {
    width: 1200px; height: 900px; overflow: hidden;
    background: var(--backdrop);
    font-family: "Open Sans", Arial, sans-serif;
  }
  .canvas { position: relative; width: 1200px; height: 900px; }
  .card {
    position: absolute;
    background: radial-gradient(ellipse at 50% 40%, #2f3a44 0%, var(--card) 55%, var(--card-edge) 100%);
    box-shadow: 0 6px 18px rgba(0,0,0,0.18);
  }
  .card--front { left: 238px; top: 62px; width: 555px; height: 342px; }
  .card--back  { left: 457px; top: 518px; width: 560px; height: 343px; }

  .brand {
    position: absolute;
    display: flex; align-items: center; gap: 12px;
    color: var(--accent);
    font-weight: 600;
    text-transform: uppercase;
    letter-spacing: 2.5px;
    line-height: 1.3;
    white-space: nowrap;
  }
  .brand__dot {
    width: 14px; height: 14px; border-radius: 50%;
    background: var(--accent); flex: none;
  }
  .brand__name { display: flex; flex-direction: column; }
  .card--front .brand { left: 44px; top: 120px; font-size: 18px; }
  .card--back .brand {
    left: 50%; top: 145px; transform: translateX(-50%);
    font-size: 20px;
  }

  .contact {
    position: absolute; right: 46px; top: 152px;
    text-align: right; color: var(--text-soft);
    font-size: 14.5px; line-height: 20px;
  }
  .contact__name {
    color: var(--text); font-weight: 600; font-size: 20px;
    line-height: 24px;
    margin-bottom: 12px; letter-spacing: 0.3px;
  }
  .contact__address { margin-bottom: 12px; }
  .contact__line { display: flex; justify-content: flex-end; align-items: center; gap: 8px; }
  .contact__icon { width: 11px; height: 11px; flex: none; fill: var(--text); }
</style>
</head>
<body>
<main class="canvas">

  <section class="card card--front" aria-label="Business card front">
    <div class="brand">
      <span class="brand__dot"></span>
      <span class="brand__name"><span>Dalton</span><span>Wire Supply, Inc.</span></span>
    </div>

    <div class="contact">
      <p class="contact__name">DALTON</p>
      <div class="contact__address">
        <p>418 Birchwood Lane</p>
        <p>Millbrook, VA 24512</p>
      </div>
      <p class="contact__line">540-555-2741
        <svg class="contact__icon" viewBox="0 0 24 24" aria-label="Phone"><path d="M6.6 10.8a15.1 15.1 0 0 0 6.6 6.6l2.2-2.2a1 1 0 0 1 1-.25 11.4 11.4 0 0 0 3.6.57 1 1 0 0 1 1 1V20a1 1 0 0 1-1 1A17 17 0 0 1 3 4a1 1 0 0 1 1-1h3.5a1 1 0 0 1 1 1c0 1.25.2 2.45.57 3.57a1 1 0 0 1-.25 1z"/></svg>
      </p>
      <p class="contact__line">540-555-8196
        <svg class="contact__icon" viewBox="0 0 24 24" aria-label="Fax"><path d="M7 2h8l3 3v5H7z M4 11h16a2 2 0 0 1 2 2v9H2v-9a2 2 0 0 1 2-2z M7 15v2h4v-2z"/></svg>
      </p>
      <p class="contact__line">daltonwire@pinemail.example
        <svg class="contact__icon" viewBox="0 0 24 24" aria-label="Email"><path d="M2 5h20v14H2z M3.5 6.5 12 13l8.5-6.5" stroke="var(--card)" stroke-width="1.6" fill="var(--text)"/></svg>
      </p>
    </div>
  </section>

  <section class="card card--back" aria-label="Business card back">
    <div class="brand">
      <span class="brand__dot"></span>
      <span class="brand__name"><span>Dalton</span><span>Wire Supply, Inc.</span></span>
    </div>
  </section>

</main>
</body>
</html>
```